TKA Electricial Contracting Services

Hi guys, after a design for my small electrical company, have logo design files to be incorporated into the layout, the basic concept is electrical contracting services for residential, commercial, industrial & data services, image is clean clear and strong,

Card format is to have a nice clean logo on front,with maybe the Residential – commercial – industrial - data, followed with licensed & insured, followed by contact details on backside of the card.

Target Market(s)

Residential, commercial, industrial sectors.

Industry/Entity Type

Electrical

Contact Information for Business Card

TKA logo,
Residential – commercial – industrial - data
REC: 61372
Email: tka@poralink.net.au
Phone: 0458 203 719

Requirements
Must have
• Clean & strong design.
Nice to have
• If possible, I would like the logo colours inverted so the text is orange and the background is black on the front of the card, then the backside of the card be the reverse colour
Should not have
• No Sparks, lightning bolts,

```html
<!DOCTYPE html>
<html lang="en">
<head>
<meta charset="utf-8">
<title>TKA Electrical Contracting Services – Business Card</title>
<link rel="stylesheet" href="https://fonts.googleapis.com/css2?family=Exo+2:wght@600&display=swap">
<style>
  :root {
    --stage: #ececec;
    --orange: #ee8536;
    --charcoal: #232323;
    --card-shadow: rgba(0, 0, 0, 0.18);
  }
  * { box-sizing: border-box; margin: 0; padding: 0; }
  html, body {
    width: 1200px;
    height: 800px;
    overflow: hidden;
    background: var(--stage);
    font-family: "Exo 2", "Segoe UI", sans-serif;
    font-weight: 600;
  }
  .stage {
    position: relative;
    width: 1200px;
    height: 800px;
  }
  .card {
    position: absolute;
    width: 500px;
    height: 300px;
    border-radius: 3px;
    box-shadow: 0 6px 16px var(--card-shadow);
    display: flex;
    align-items: center;
    justify-content: center;
  }
  .card--back {
    left: 90px;
    top: 80px;
    background: var(--orange);
    color: var(--charcoal);
  }
  .card--front {
    left: 610px;
    top: 420px;
    background: var(--charcoal);
    color: var(--orange);
  }
  .card__content {
    width: 240px;
    display: flex;
    flex-direction: column;
  }
  .brand-name {
    font-size: 56px;
    line-height: 1;
    letter-spacing: 2px;
  }
  .company-name {
    font-size: 15px;
    margin-top: 6px;
    letter-spacing: 0.3px;
  }
  .contact-list {
    list-style: none;
    margin-top: 8px;
  }
  .contact-list__item {
    display: flex;
    align-items: center;
    gap: 8px;
    line-height: 1.3;
  }
  .contact-list__item--phone { font-size: 21px; }
  .contact-list__item--email { font-size: 17px; }
  .contact-list__icon {
    width: 16px;
    height: 16px;
    flex: none;
  }
  .services {
    font-size: 16px;
    line-height: 1.25;
    margin-top: 8px;
  }
  .licence-bar {
    margin-top: 10px;
    height: 15px;
    font-size: 11px;
    line-height: 15px;
    padding-left: 10px;
    letter-spacing: 0.5px;
  }
  .card--back .licence-bar { background: var(--charcoal); color: var(--orange); }
  .card--front .licence-bar { background: var(--orange); color: var(--charcoal); }
</style>
</head>
<body>
<main class="stage">
  <section class="card card--back" aria-label="Business card, contact side">
    <div class="card__content">
      <p class="brand-name">TKA</p>
      <p class="company-name">Tom Kendall Electrical</p>
      <ul class="contact-list">
        <li class="contact-list__item contact-list__item--phone">
          <svg class="contact-list__icon" viewBox="0 0 16 16" aria-hidden="true">
            <path d="M3.5 1.5l2.5 0.5 1 3-1.6 1.2c0.8 1.7 2.2 3.1 3.9 3.9L10.5 8.5l3 1 0.5 2.5-1.5 2C7 14 2 9 1.5 3z" fill="currentColor"/>
          </svg>
          <span>0458 203 719</span>
        </li>
        <li class="contact-list__item contact-list__item--email">
          <svg class="contact-list__icon" viewBox="0 0 16 16" aria-hidden="true">
            <rect x="1" y="3" width="14" height="10" fill="none" stroke="currentColor" stroke-width="1.6"/>
            <path d="M1 3l7 6 7-6" fill="none" stroke="currentColor" stroke-width="1.6"/>
          </svg>
          <span>tka@poralink.net.au</span>
        </li>
      </ul>
      <div class="licence-bar">REC. 61372</div>
    </div>
  </section>

  <section class="card card--front" aria-label="Business card, logo side">
    <div class="card__content">
      <p class="brand-name">TKA</p>
      <p class="company-name">Tom Kendall Electrical</p>
      <p class="services">Residential, Commercial<br>Industrial &amp; Data Services</p>
      <div class="licence-bar">REC. 61372</div>
    </div>
  </section>
</main>
</body>
</html>
```